Vesk Architecture

We are a architectural design and build company working between scales 1/1000 to 1/1 we want people to understand our difference from our design experience and quality.we build hotels restourants and office spaces.Our company name is Vesk architecture to mind sustainability.

We want to write our adress phone and work spesifications on the card and we want our logo as backround.

Ps:you could find the logo adress and phone box numbers from the web:www.veskmimarlik-ornek.com

Target Market(s)

Who looks for experts.

Industry/Entity Type

Architecture

Requirements
Must have
• Design is over everything.
Should not have
• we don want it to be colorfull

```html
<!DOCTYPE html>
<html lang="tr">
<head>
<meta charset="utf-8">
<title>Vesk Mimarlik – Business Card</title>
<link href="https://fonts.googleapis.com/css2?family=Josefin+Sans:wght@300&family=Cinzel:wght@500&display=swap" rel="stylesheet">
<style>
  :root {
    --stage: #f3f3f5;
    --sheet: #ffffff;
    --teal: #2bbcb2;
    --ink: #111111;
    --rule: #8a8a8a;
    --shadow: rgba(0,0,0,0.18);
  }
  html, body {
    margin: 0;
    width: 1200px;
    height: 900px;
    overflow: hidden;
    background: var(--sheet);
  }
  .canvas {
    position: relative;
    width: 1200px;
    height: 900px;
  }
  .stage {
    position: absolute;
    left: 158px; top: 55px;
    width: 867px; height: 783px;
    background: var(--stage);
  }
  .sheet {
    position: absolute;
    left: 215px; top: 55px;
    width: 750px; height: 783px;
    background: var(--sheet);
  }
  .card {
    position: absolute;
    box-shadow: 0 8px 14px var(--shadow);
  }
  .card--front {
    left: 246px; top: 88px;
    width: 684px; height: 340px;
    border-radius: 22px;
    overflow: hidden;
  }
  .card--front .card__bg {
    position: absolute; inset: 0;
  }
  .card--back {
    left: 242px; top: 466px;
    width: 694px; height: 349px;
    border-radius: 28px;
    background: var(--teal);
  }
  .divider {
    position: absolute;
    left: 299px; top: 34px;
    width: 2px; height: 276px;
    background: var(--rule);
  }
  .wordmark {
    position: absolute;
    font-family: "Josefin Sans", sans-serif;
    font-weight: 300;
    color: var(--ink);
    margin: 0;
    line-height: 1;
  }
  .wordmark__name { display: block; }
  .wordmark__sub {
    display: block;
    letter-spacing: 0.12em;
  }
  .card--front .wordmark { left: 76px; top: 108px; }
  .card--front .wordmark__name { font-size: 78px; letter-spacing: 0.02em; }
  .card--front .wordmark__sub { font-size: 17px; margin-top: 6px; }
  .card--back .wordmark { left: 232px; top: 112px; }
  .card--back .wordmark__name { font-size: 92px; letter-spacing: 0.02em; }
  .card--back .wordmark__sub { font-size: 21px; margin-top: 4px; }
  .contact {
    position: absolute;
    left: 319px; top: 108px;
    margin: 0;
    font-family: "Cinzel", serif;
    font-weight: 500;
    font-size: 13px;
    line-height: 17px;
    color: var(--ink);
    font-style: normal;
    white-space: nowrap;
  }
  .contact span { display: block; }
</style>
</head>
<body>
<div class="canvas">
  <div class="stage"></div>
  <div class="sheet"></div>

  <section class="card card--front" aria-label="Card front">
    <svg class="card__bg" width="684" height="340" viewBox="0 0 684 340" aria-hidden="true">
      <rect width="684" height="340" fill="var(--teal)"/>
      <path d="M59,0 Q15,170 59,340 L626,340 Q692,170 626,0 Z" fill="var(--sheet)"/>
    </svg>
    <h1 class="wordmark">
      <span class="wordmark__name">vesk</span>
      <span class="wordmark__sub">MİMARLIK</span>
    </h1>
    <div class="divider"></div>
    <address class="contact">
      <span>Deniz Arman YILMAZ - Mimar</span>
      <span>Yelken Mah. Rihtim Cad. Liman Sok.</span>
      <span>NO : 7 Kadikoy / ISTANBUL</span>
      <span>Tel : 0216 555 0142</span>
      <span>Fax : 0216 555 0178</span>
      <span>E-mail : veskmimarlik@ornek-posta.com</span>
    </address>
  </section>

  <section class="card card--back" aria-label="Card back">
    <div class="wordmark">
      <span class="wordmark__name">vesk</span>
      <span class="wordmark__sub">MIMARLIK</span>
    </div>
  </section>
</div>
</body>
</html>
```